ALL TEXT Social Media Graphics

We are looking for a series of social media graphics for Instagram (new size: 4:5 (1080 x 1350 pixels) ratio that are ALL TEXT. We want the following quotes below on each graphic; one quote per graphic. AND, In very small letters at the bottom of each graphic, add @PaulaWrenLive
The look and feel of these graphics should be complimentary to the color palette attached below; but keep them simple. But the design is up to you; at the end of this document, I provided various samples of all text graphics that I like as examples.
The Quotes are in the attached WORD document
women trying to lose weight

```html
<!DOCTYPE html>
<html lang="en">
<head>
<meta charset="utf-8">
<title>Glow Girl Summer Shapeup – Social Graphics</title>
<link href="https://fonts.googleapis.com/css2?family=Anton&family=Poppins:ital,wght@0,300;0,700;1,700&family=Roboto:ital,wght@0,300;0,400;0,700;1,700&display=swap" rel="stylesheet">
<style>
  :root {
    --canvas: #d9d9d9;
    --card-top: #ffffff;
    --card-bottom: #fce3ed;
    --frame: #f6c3d6;
    --magenta: #b2135d;
    --pink: #ec5593;
    --ink: #1f1f1f;
    --highlight: #ee5a95;
    --white: #ffffff;
  }
  * { margin: 0; padding: 0; box-sizing: border-box; }
  html, body { width: 1200px; height: 320px; overflow: hidden; }
  body { background: var(--canvas); position: relative; font-family: 'Roboto', sans-serif; }

  .post {
    position: absolute; top: 31px; width: 207px; height: 258px;
    background: linear-gradient(180deg, var(--card-top) 55%, var(--card-bottom) 100%);
    box-shadow: 0 1px 3px rgba(0,0,0,0.08);
  }
  .post::before {
    content: ""; position: absolute; inset: 6.5px;
    border: 0.8px solid var(--frame);
  }
  .post--1 { left: 32px; }
  .post--2 { left: 264px; }
  .post--3 { left: 497px; }
  .post--4 { left: 729px; }
  .post--5 { left: 962px; }

  .block { position: absolute; left: 16px; right: 12px; white-space: nowrap; }
  .handle {
    position: absolute; left: 0; right: 0; bottom: 12px;
    text-align: center; font-family: 'Poppins', sans-serif; font-size: 3.8px; color: var(--ink);
  }

  /* Post 1 */
  .post--1 .headline { top: 14px; font-family: 'Poppins', sans-serif; font-weight: 700; font-size: 18.2px; line-height: 23px; color: var(--magenta); text-transform: uppercase; }
  .post--1 .lede { top: 134px; font-family: 'Poppins', sans-serif; font-weight: 700; font-size: 12.8px; line-height: 15.2px; color: var(--ink); }
  .post--1 .cta { top: 184px; font-family: 'Poppins', sans-serif; font-weight: 300; font-size: 12.8px; line-height: 15.4px; color: var(--pink); }
  .post--1 .cta strong { font-weight: 700; color: var(--magenta); }

  /* Posts 2 & 3 */
  .condensed-head { top: 20px; font-family: 'Anton', sans-serif; font-size: 19.4px; line-height: 23px; color: var(--magenta); text-transform: uppercase; }
  .light-body { top: 124px; font-family: 'Roboto', sans-serif; font-weight: 300; font-size: 14px; line-height: 15.4px; color: var(--ink); }
  .condensed-cta { top: 179px; font-family: 'Anton', sans-serif; font-size: 15.4px; line-height: 17.5px; color: var(--pink); }
  .post--2 .block { text-align: center; left: 10px; right: 10px; }
  .post--3 .block { text-align: right; left: 10px; right: 23px; }

  /* Post 4 */
  .post--4 .block { text-align: center; left: 8px; right: 8px; }
  .post--4 .headline { top: 33px; font-family: 'Poppins', sans-serif; font-weight: 300; font-size: 17.6px; line-height: 23px; color: var(--magenta); text-transform: uppercase; }
  .post--4 .cta { top: 160px; font-family: 'Roboto', sans-serif; font-weight: 700; font-size: 13.2px; line-height: 15.4px; color: var(--ink); }
  .post--4 .cta span { color: var(--pink); font-weight: 400; }

  /* Post 5 */
  .post--5 .block { text-align: center; left: 8px; right: 8px; }
  .post--5 .headline { top: 23px; font-family: 'Poppins', sans-serif; font-weight: 700; font-size: 17.8px; line-height: 23px; color: var(--magenta); text-transform: uppercase; }
  .mark { background: var(--highlight); color: var(--white); padding: 0 3px; }
  .post--5 .lede { top: 159px; font-family: 'Roboto', sans-serif; font-weight: 700; font-size: 13px; line-height: 15.2px; color: var(--ink); text-transform: uppercase; }
  .post--5 .lede .mark em { font-style: italic; }
</style>
</head>
<body>

<article class="post post--1">
  <h2 class="block headline">You can<br>absolutely<br>be down 20–30<br>pounds by end<br>of summer.</h2>
  <p class="block lede">All it takes is the right<br>plan—and you’ve<br>found it.</p>
  <p class="block cta">Comment <strong>“Glow Girl”</strong> for<br>the Glow Girl Summer<br>Shapeup!</p>
  <p class="handle">@PaulaWrenLive</p>
</article>

<article class="post post--2">
  <h2 class="block condensed-head">You don’t need<br>another diet—you<br>need a system<br>that works.</h2>
  <p class="block light-body">Drop 30 pounds with the<br>Glow Girl Summer<br>Shapeup.</p>
  <p class="block condensed-cta">Comment “Summer”<br>to start now.</p>
  <p class="handle">@PaulaWrenLive</p>
</article>

<article class="post post--3">
  <h2 class="block condensed-head">This summer ain’t<br>over—and neither<br>are your body<br>goals.</h2>
  <p class="block light-body">Drop 30 pounds with the<br>Glow Girl Summer<br>Shapeup.</p>
  <p class="block condensed-cta">Comment “Glow Girl” to<br>get the plan</p>
  <p class="handle">@PaulaWrenLive</p>
</article>

<article class="post post--4">
  <h2 class="block headline">If your goal is<br>a tiny waist,<br>flat belly, and 30<br>pounds down<br>—this is the plan.</h2>
  <p class="block cta">Comment <span>“Summer”</span><br>to join the Glow Girl<br>Summer Shapeup!</p>
  <p class="handle">@PaulaWrenLive</p>
</article>

<article class="post post--5">
  <h2 class="block headline">There’s still<br>time to drop<br><span class="mark">the 30 pounds</span><br>and slay<br>this summer.</h2>
  <p class="block lede">The Glow Girl Summer<br>Shapeup has the<br>blueprint.<br><span class="mark">Comment <em>“Glow Girl”!</em></span></p>
  <p class="handle">@PaulaWrenLive</p>
</article>

</body>
</html>
```